Coloring book cover design: Shade Me, Bend Me coloring book, Christmas edition Volume 1

I need a cover design [front and back please]] (book trim size: 8.5 x 11 inches) for my first coloring book titled "Shade me, bend me: coloring book (Christmas Edition)". The designs should include Christmassy colors (for example: green, red, gold and/or other colors but not more than 5 in total). Covers need to be sufficiently generic to maintain a recognizable design theme for other non-Christmassy forthcoming books/editions (i.e. familiar design theme across all books so customers know they come from the same author).
Updates

I have increased the budget for the 1st prize and updated the brief. This is the first in a series of books and the designs need to create a theme that is then repeated across future editions and volumes. Added Friday, August 26, 2016

Target Market(s)

Mostly women (age: 25+).

Industry/Entity Type

Graphic Art

Font styles to use
Serif
Sans Serif
Decorative

Requirements
Must have
• The cover design must include designs provided in separate JPEG/PSD files (these are from the book itself) so customers can sense what to expect from the book’s content. The supplied PSD files include paths so please play around with supplied files and take some motives from the overall patterns.
Nice to have
• Some nice features that will make it stand out from the crowd of recent coloring book covers. I will let the designer choose the colors but as stated, they have to be Christmassy.
• Some good examples from Greta Vollins and Daphne Runstedt:
• https://media-eu.cdn-pictures-bravoshop.example/img/P/72qd5mMhcEK._TX369_CP2,315,314,311_.jpg
• http://quietbrushwork.example/wp-content/uploads/2015/03/Screenshot-2015-12-16-12.07.06.png
Should not have
• Imported images of people, animals, etc. This is a coloring book and the cover must reflect this.

```html
<!DOCTYPE html>
<html lang="en">
<head>
<meta charset="utf-8">
<title>Shade Me, Bend Me – Christmas Edition Volume 1</title>
<link rel="stylesheet" href="https://fonts.googleapis.com/css2?family=Source+Sans+3:wght@400;600&family=Sniglet:wght@400;800&display=swap">
<style>
  :root {
    --ice-blue: #7fd3ee;
    --sky-blue: #b9e8f7;
    --frost: #eef8fc;
    --blush: #f6c9cf;
    --peach: #f7b59e;
    --ink: #161616;
    --teal: #3c8fa8;
    --crimson: #d91e26;
    --deep-red: #6e0a0a;
    --white: #ffffff;
    --navy: #1f3f66;
    --line-white: rgba(255,255,255,0.85);
    --line-soft: rgba(255,255,255,0.55);
  }
  * { margin: 0; padding: 0; box-sizing: border-box; }
  html, body { width: 927px; height: 1200px; overflow: hidden; background: var(--white); }

  .cover {
    position: relative;
    width: 927px;
    height: 1200px;
    overflow: hidden;
    background:
      radial-gradient(circle at 78% 30%, rgba(247,181,158,0.75) 0%, rgba(246,201,207,0.55) 22%, rgba(246,201,207,0) 45%),
      radial-gradient(circle at 50% 50%, var(--frost) 0%, rgba(238,248,252,0.6) 30%, rgba(238,248,252,0) 60%),
      linear-gradient(90deg, var(--ice-blue) 0%, var(--sky-blue) 40%, var(--blush) 70%, var(--sky-blue) 100%);
  }

  .pattern-field {
    position: absolute;
    inset: 0;
    background: radial-gradient(circle at 50% 51%, rgba(255,255,255,0.35) 0%, rgba(255,255,255,0.15) 40%, rgba(255,255,255,0) 70%);
  }

  .line-frame {
    position: absolute;
    inset: 0;
    width: 927px;
    height: 1200px;
    fill: none;
  }
  .line-frame .ring { stroke: var(--line-white); stroke-width: 2; }
  .line-frame .ring--thin { stroke: var(--line-soft); stroke-width: 1.2; }
  .line-frame .spoke { stroke: var(--line-soft); stroke-width: 1.2; }
  .line-frame .corner-arc { stroke: var(--line-soft); stroke-width: 1.5; }

  .series-line {
    position: absolute;
    top: 46px;
    left: 343px;
    font-family: "Source Sans 3", sans-serif;
    font-weight: 600;
    font-size: 27px;
    letter-spacing: 4.6px;
    background: linear-gradient(90deg, var(--navy), #5a3a5a 60%, var(--crimson));
    -webkit-background-clip: text;
    background-clip: text;
    color: transparent;
  }
  .volume-tag {
    position: absolute;
    top: 35px;
    left: 686px;
    width: 241px;
    height: 50px;
    background: linear-gradient(90deg, var(--crimson) 60%, var(--deep-red));
    color: var(--white);
    font-family: "Source Sans 3", sans-serif;
    font-size: 32px;
    letter-spacing: 3px;
    line-height: 50px;
    padding-left: 13px;
  }

  .rosette {
    position: absolute;
    width: 82px;
    height: 82px;
    border-radius: 50%;
  }
  .rosette--blue { background: radial-gradient(circle, #a6e4fb 0%, #3fb0e4 70%, #8fd3ef 100%); }
  .rosette--dark { background: radial-gradient(circle, #8c959c 0%, #25292d 70%, #5a6168 100%); }
  .rosette--coral { background: radial-gradient(circle, #f8c6b2 0%, #e0573a 70%, #f09a80 100%); }
  .rosette--red { background: radial-gradient(circle, #f6b1a5 0%, #d8392d 70%, #ee8b7f 100%); }
  .rosette-rings { position: absolute; inset: 0; width: 82px; height: 82px; fill: none; stroke: rgba(255,255,255,0.45); stroke-width: 1; }

  .title-badge {
    position: absolute;
    left: 266px;
    top: 414px;
    width: 394px;
    height: 394px;
    border-radius: 50%;
    background: var(--white);
    box-shadow: 0 0 16px rgba(120,140,160,0.35);
  }
  .santa-hat {
    position: absolute;
    left: 340px;
    top: 462px;
    width: 72px;
    height: 60px;
  }
  .book-kind {
    position: absolute;
    left: 430px;
    top: 500px;
    font-family: "Source Sans 3", sans-serif;
    font-weight: 600;
    font-size: 28px;
    letter-spacing: -0.3px;
  }
  .book-kind span:nth-child(1) { color: #e43b2e; }
  .book-kind span:nth-child(2) { color: #f08a1d; }
  .book-kind span:nth-child(3) { color: #e5b51c; }
  .book-kind span:nth-child(4) { color: #3aa43b; }
  .book-kind span:nth-child(5) { color: #2e9fce; }
  .book-kind span:nth-child(6) { color: #2a56b8; }
  .book-kind span:nth-child(7) { color: #6b3ab0; }

  .book-title {
    position: absolute;
    left: 266px;
    top: 532px;
    width: 394px;
    text-align: center;
    font-family: "Sniglet", cursive;
    font-weight: 400;
    font-size: 70px;
    line-height: 84px;
    letter-spacing: 1px;
  }
  .book-title .title-line { display: block; -webkit-background-clip: text; background-clip: text; color: transparent; }
  .book-title .title-line--first { background-image: linear-gradient(90deg, var(--ink) 0%, #3a2a2a 45%, #8a4a52 65%, var(--teal) 100%); }
  .book-title .title-line--second { background-image: linear-gradient(90deg, var(--ink) 0%, #5a1414 40%, var(--crimson) 70%, #4a2a6a 100%); }

  .author {
    position: absolute;
    left: 266px;
    top: 700px;
    width: 394px;
    text-align: center;
    font-family: "Source Sans 3", sans-serif;
    font-size: 32px;
    letter-spacing: 1.6px;
    color: var(--ink);
  }
  .author .surname { color: var(--crimson); }
</style>
</head>
<body>
<main class="cover">
  <div class="pattern-field" role="img" aria-label="Soft frosted mandala and snowflake coloring-page pattern across the cover"></div>

  <svg class="line-frame" viewBox="0 0 927 1200" aria-hidden="true">
    <circle class="ring" cx="463" cy="611" r="312"/>
    <circle class="ring--thin" cx="463" cy="611" r="296"/>
    <circle class="ring--thin" cx="463" cy="611" r="250"/>
    <circle class="ring--thin" cx="463" cy="611" r="214"/>
    <circle class="ring--thin" cx="463" cy="611" r="400"/>
    <line class="spoke" x1="463" y1="256" x2="463" y2="414"/>
    <line class="spoke" x1="463" y1="808" x2="463" y2="974"/>
    <line class="spoke" x1="109" y1="605" x2="266" y2="608"/>
    <line class="spoke" x1="660" y1="608" x2="814" y2="603"/>
    <line class="spoke" x1="213" y1="359" x2="325" y2="470"/>
    <line class="spoke" x1="708" y1="354" x2="601" y2="470"/>
    <line class="spoke" x1="213" y1="866" x2="325" y2="752"/>
    <line class="spoke" x1="725" y1="850" x2="601" y2="752"/>
    <line class="spoke" x1="463" y1="0" x2="463" y2="174"/>
    <line class="spoke" x1="463" y1="1056" x2="463" y2="1200"/>
    <line class="spoke" x1="0" y1="605" x2="27" y2="605"/>
    <line class="spoke" x1="896" y1="603" x2="927" y2="603"/>
    <circle class="corner-arc" cx="0" cy="0" r="230"/>
    <circle class="corner-arc" cx="0" cy="0" r="180"/>
    <circle class="corner-arc" cx="927" cy="0" r="230"/>
    <circle class="corner-arc" cx="927" cy="0" r="180"/>
    <circle class="corner-arc" cx="0" cy="1200" r="260"/>
    <circle class="corner-arc" cx="0" cy="1200" r="200"/>
    <circle class="corner-arc" cx="927" cy="1200" r="260"/>
    <circle class="corner-arc" cx="927" cy="1200" r="200"/>
    <line class="spoke" x1="0" y1="440" x2="200" y2="440"/>
    <line class="spoke" x1="727" y1="440" x2="927" y2="440"/>
    <line class="spoke" x1="0" y1="770" x2="200" y2="770"/>
    <line class="spoke" x1="727" y1="770" x2="927" y2="770"/>
  </svg>

  <div class="series-line">CHRISTMAS EDITION</div>
  <div class="volume-tag">VOLUME 1</div>

  <div class="rosette rosette--blue" style="left:421px;top:174px" role="img" aria-label="Blue mandala rosette"><svg class="rosette-rings" viewBox="0 0 82 82"><circle cx="41" cy="41" r="36"/><circle cx="41" cy="41" r="26"/><circle cx="41" cy="41" r="14"/><circle cx="41" cy="41" r="5"/></svg></div>
  <div class="rosette rosette--dark" style="left:141px;top:289px" role="img" aria-label="Charcoal mandala rosette"><svg class="rosette-rings" viewBox="0 0 82 82"><circle cx="41" cy="41" r="36"/><circle cx="41" cy="41" r="26"/><circle cx="41" cy="41" r="14"/><circle cx="41" cy="41" r="5"/></svg></div>
  <div class="rosette rosette--coral" style="left:696px;top:284px" role="img" aria-label="Coral mandala rosette"><svg class="rosette-rings" viewBox="0 0 82 82"><circle cx="41" cy="41" r="36"/><circle cx="41" cy="41" r="26"/><circle cx="41" cy="41" r="14"/><circle cx="41" cy="41" r="5"/></svg></div>
  <div class="rosette rosette--dark" style="left:27px;top:564px" role="img" aria-label="Charcoal mandala rosette"><svg class="rosette-rings" viewBox="0 0 82 82"><circle cx="41" cy="41" r="36"/><circle cx="41" cy="41" r="26"/><circle cx="41" cy="41" r="14"/><circle cx="41" cy="41" r="5"/></svg></div>
  <div class="rosette rosette--blue" style="left:814px;top:562px" role="img" aria-label="Blue mandala rosette"><svg class="rosette-rings" viewBox="0 0 82 82"><circle cx="41" cy="41" r="36"/><circle cx="41" cy="41" r="26"/><circle cx="41" cy="41" r="14"/><circle cx="41" cy="41" r="5"/></svg></div>
  <div class="rosette rosette--dark" style="left:141px;top:854px" role="img" aria-label="Charcoal mandala rosette"><svg class="rosette-rings" viewBox="0 0 82 82"><circle cx="41" cy="41" r="36"/><circle cx="41" cy="41" r="26"/><circle cx="41" cy="41" r="14"/><circle cx="41" cy="41" r="5"/></svg></div>
  <div class="rosette rosette--red" style="left:714px;top:839px" role="img" aria-label="Red mandala rosette"><svg class="rosette-rings" viewBox="0 0 82 82"><circle cx="41" cy="41" r="36"/><circle cx="41" cy="41" r="26"/><circle cx="41" cy="41" r="14"/><circle cx="41" cy="41" r="5"/></svg></div>
  <div class="rosette rosette--dark" style="left:421px;top:974px" role="img" aria-label="Charcoal mandala rosette"><svg class="rosette-rings" viewBox="0 0 82 82"><circle cx="41" cy="41" r="36"/><circle cx="41" cy="41" r="26"/><circle cx="41" cy="41" r="14"/><circle cx="41" cy="41" r="5"/></svg></div>

  <div class="title-badge"></div>

  <svg class="santa-hat" viewBox="0 0 72 60" role="img" aria-label="Small Santa hat illustration">
    <path d="M4 44 C10 20 30 4 52 10 C60 14 62 26 66 40 Z" fill="#c8161d"/>
    <rect x="2" y="40" width="58" height="14" rx="7" fill="#f2f2f2"/>
    <circle cx="66" cy="42" r="6" fill="#f2f2f2"/>
  </svg>

  <div class="book-kind"><span>co</span><span>lo</span><span>ri</span><span>ng</span><span> bo</span><span>o</span><span>k</span></div>

  <h1 class="book-title">
    <span class="title-line title-line--first">shade me</span>
    <span class="title-line title-line--second">bend me</span>
  </h1>

  <p class="author">CORAL <span class="surname">FINCH</span></p>
</main>
</body>
</html>
```